I am wanting to develop a new range of products called “SWIFT LINE”. It will be 500mL trigger bottles of ready to use cleaning products. A Window&Glass Cleaner, Surface Sanitiser, Room Deodourant, Stainless Steel Rub, Spray&Wipe and a Sanitising Spray & Wipe. The label dimensions and shape are attached. Marlow is the shape I want but I do not like the design so don't base your design on it. FRESHDASH is a design I like I also like the design on the coffee packaging.

Retail and commercial kitchen

Cleaning Product

```html
<!DOCTYPE html>
<html lang="en">
<head>
<meta charset="utf-8">
<title>Swift Line – Surface Sanitiser Label</title>
<link href="https://fonts.googleapis.com/css2?family=Montserrat:wght@400;700;800&family=Russo+One&display=swap" rel="stylesheet">
<style>
  :root {
    --wood-light: #a87a52;
    --wood-mid: #946643;
    --wood-dark: #7a5234;
    --label-green: #4a9a1f;
    --splash-light: rgba(235, 255, 225, 0.5);
    --title-yellow: #fff200;
    --title-yellow-deep: #f2d600;
    --title-navy: #0f2340;
    --white: #ffffff;
    --ink: #111111;
  }
  html, body {
    margin: 0;
    padding: 0;
    overflow: hidden;
    background: #ffffff;
  }
  .label {
    position: relative;
    width: 935px;
    height: 1200px;
    overflow: hidden;
    background: var(--label-green);
    font-family: "Montserrat", Arial, sans-serif;
  }
  .wood-panel {
    position: absolute;
    left: 0; top: 0;
    width: 935px; height: 597px;
    background: linear-gradient(160deg, var(--wood-light) 0%, var(--wood-mid) 45%, var(--wood-dark) 100%);
  }
  .splash-area {
    position: absolute;
    left: 0; top: 860px;
    width: 935px; height: 340px;
    background:
      radial-gradient(ellipse 50% 45% at 42% 55%, var(--splash-light) 0%, rgba(235,255,225,0.18) 55%, rgba(235,255,225,0) 80%),
      linear-gradient(to bottom, rgba(255,255,255,0) 78%, rgba(200,240,190,0.3) 100%);
  }
  .brand {
    position: absolute;
    right: 102px; top: 80px;
    display: flex;
    align-items: center;
    gap: 12px;
    color: var(--white);
    font-weight: 800;
    font-size: 42px;
    line-height: 1;
  }
  .brand-dot {
    width: 26px; height: 26px;
    border-radius: 50%;
    background: var(--white);
  }
  .range-title {
    position: absolute;
    left: 0; top: 0;
    width: 935px; height: 1200px;
    margin: 0;
  }
  .range-title text {
    font-family: "Russo One", "Arial Black", sans-serif;
    font-size: 240px;
  }
  .title-outer { fill: var(--white); stroke: var(--white); stroke-width: 48px; stroke-linejoin: round; }
  .title-edge { fill: var(--title-navy); stroke: var(--title-navy); stroke-width: 28px; stroke-linejoin: round; }
  .title-face { fill: url(#titleFill); }
  .product-name {
    position: absolute;
    right: 84px; top: 750px;
    margin: 0;
    color: var(--white);
    font-size: 46px;
    font-weight: 400;
    line-height: 1;
    white-space: nowrap;
  }
  .product-name strong { font-weight: 800; }
  .benefits {
    position: absolute;
    right: 84px; top: 852px;
    margin: 0; padding: 0;
    list-style: none;
    text-align: right;
    color: var(--white);
    font-size: 33px;
    line-height: 37px;
    white-space: nowrap;
  }
  .benefits strong { font-weight: 800; }
  .volume {
    position: absolute;
    left: 394px; top: 1094px;
    color: var(--ink);
    font-weight: 800;
    font-size: 40px;
    line-height: 1;
  }
</style>
</head>
<body>
  <main class="label">
    <div class="wood-panel" role="img" aria-label="Photograph of an oak wood surface"></div>
    <div class="splash-area" role="img" aria-label="Photograph of a clear water splash"></div>

    <div class="brand">
      <span class="brand-dot"></span>
      <span class="brand-name">Tidewren</span>
    </div>

    <svg class="range-title" viewBox="0 0 935 1200" role="img" aria-label="SWIFT LINE">
      <defs>
        <linearGradient id="titleFill" x1="0" y1="0" x2="0" y2="1">
          <stop offset="0" stop-color="#fff200"/>
          <stop offset="1" stop-color="#f2d600"/>
        </linearGradient>
        <filter id="titleShadow" x="-10%" y="-10%" width="130%" height="140%">
          <feDropShadow dx="8" dy="12" stdDeviation="8" flood-color="#000" flood-opacity="0.4"/>
        </filter>
      </defs>
      <g transform="rotate(-10 146 515)">
        <text class="title-outer" x="146" y="515" textLength="565" lengthAdjust="spacingAndGlyphs" filter="url(#titleShadow)">SWIFT</text>
        <text class="title-edge" x="146" y="515" textLength="565" lengthAdjust="spacingAndGlyphs">SWIFT</text>
        <text class="title-face" x="146" y="515" textLength="565" lengthAdjust="spacingAndGlyphs">SWIFT</text>
      </g>
      <g transform="rotate(-10 298 690)">
        <text class="title-outer" x="298" y="690" textLength="530" lengthAdjust="spacingAndGlyphs" filter="url(#titleShadow)">LINE</text>
        <text class="title-edge" x="298" y="690" textLength="530" lengthAdjust="spacingAndGlyphs">LINE</text>
        <text class="title-face" x="298" y="690" textLength="530" lengthAdjust="spacingAndGlyphs">LINE</text>
      </g>
    </svg>

    <h2 class="product-name"><strong>SURFACE</strong> SANITASER</h2>

    <ul class="benefits">
      <li><strong>CLEANSES</strong> MOST SURFACES</li>
      <li><strong>100%</strong> ECO-FRIENDLY</li>
      <li><strong>ANTI-</strong>BACTERIAL</li>
    </ul>

    <div class="volume">500ML</div>
  </main>
</body>
</html>
```